Landing page in the senior sector

We need a landing page for families looking for retirement homes for their parent. The target is rather old (50-60 years old). The mandatory fields are Name, Email, Phone. The optional fields are budget, research zipcode, Emergency (,,). It is important to note that this is a free service that we offer to families in research. It should be noted that they are often in distress and repulsive. Need a mobile landing We need a landing page to recruit families looking for retirement homes for their parent. The target is rather old (50-60 years old). Required fields are Name, Email, Phone. The optional fields (they may not appear at all) are Budget, Search CP, Emergency (,,). It is important to mention that this is a free service that we offer to families in search. It should be noted that they are often in distress and that asking them for input may let tel may seem repulsive. Also need a mobile version

Target Market(s)

rather old (50-60 years old) / rather old (50-60 years old)

Coding

Coded - Design and coding required

Number of Pages Required

2 page

Font styles to use
Sans Serif

Colors

Designer to choose colors to be used in the design.

Requirements
Must have
• - A form with the 3 mandatory fields / A form with the 3 mandatory fields - Optimized for conversion / Optimized for conversion

```html
<!DOCTYPE html>
<html lang="en">
<head>
<meta charset="utf-8">
<title>Harbor Years – Senior housing counselling</title>
<link rel="stylesheet" href="https://fonts.googleapis.com/css2?family=Noto+Serif&family=Open+Sans:wght@700&family=Source+Sans+3:wght@400;600;700&display=swap">
<style>
:root{
  --ink:#4a4a4a;
  --ink-soft:#666;
  --green:#5cb85c;
  --green-text:#62b76a;
  --slate:#5a656c;
  --slate-line:#555e64;
  --mist:#f4f4f4;
  --teal:#3f9680;
  --teal-dark:#2f7a68;
  --orange:#f5a00f;
  --white:#fff;
  --blue-brand:#1c6aa6;
}
*{box-sizing:border-box;margin:0;padding:0}
html,body{width:1200px;height:2489px;overflow:hidden;background:var(--white)}
body{position:relative;font-family:"Source Sans 3",sans-serif;color:var(--ink)}
.abs{position:absolute}
.serif{font-family:"Noto Serif",serif;font-weight:400}

/* header */
.site-header{position:absolute;left:0;top:0;width:1200px;height:124px;border-bottom:4px solid var(--slate-line)}
.brand{position:absolute;left:134px;top:42px;display:flex;align-items:center;gap:8px;font-weight:700;font-size:21px;color:var(--blue-brand)}
.brand-mark{width:18px;height:18px;background:var(--green);border-radius:50%}
.phone{position:absolute;right:82px;top:38px;font-family:"Open Sans",sans-serif;font-weight:700;font-size:33px;color:#111}
.main-nav{position:absolute;left:490px;top:102px;display:flex;gap:18px;font-size:15px;color:var(--ink-soft)}

/* hero */
.hero{position:absolute;left:0;top:128px;width:1188px;height:322px}
.hero-photo{position:absolute;inset:0;background:radial-gradient(ellipse at 30% 55%,#cfc6b8 0,#b7ab9a 14%,#4e9a86 30%,transparent 46%),linear-gradient(100deg,var(--teal-dark),var(--teal) 45%,#3b8f7a)}
.hero-title{position:absolute;left:596px;top:14px;font-size:24px;line-height:24px;color:var(--white)}
.hero-form .field{position:absolute;left:597px;width:252px;height:21px;background:var(--white);border:1px solid #ddd;font-size:9px;color:#666;padding:4px 3px}
.captcha{position:absolute;background:#f9f9f9;border:1px solid #d3d3d3;border-radius:3px;display:flex;align-items:center;color:#222}
.captcha .box{border:2px solid #c1c1c1;background:var(--white);border-radius:2px}
.captcha .badge{position:absolute;background:#b5c3d6;border-radius:2px}
.captcha small{position:absolute;font-size:5px;color:#777}
.send-sm{position:absolute;left:597px;top:287px;width:37px;height:22px;background:var(--white);font-size:9px;text-align:center;line-height:22px;color:#444}

/* services */
.services{position:absolute;left:0;top:450px;width:1188px;height:288px;background:var(--mist)}
.service{position:absolute;top:21px;width:214px}
.service .photo{height:122px;position:relative}
.service .photo span{position:absolute;left:8px;bottom:4px;font-size:16px;line-height:20px;color:#444}
.service p{margin-top:15px;font-size:11px;line-height:14.5px;color:var(--ink-soft)}
.btn-outline{position:absolute;border:2px solid var(--green);color:var(--green);background:transparent;text-align:center;font-size:16px}
.service .btn-outline{top:205px;width:130px;height:30px;line-height:26px}

/* why */
.section-title{position:absolute;width:1188px;text-align:center;font-size:27px;color:#555}
.feature{position:absolute;width:240px}
.feature svg{position:absolute;left:0;width:48px;height:56px}
.feature h3{position:absolute;left:57px;font-size:19px;line-height:19px;color:#555}
.feature p{position:absolute;left:57px;width:170px;font-size:11px;line-height:14.5px;color:var(--ink-soft)}

/* contact */
.contact{position:absolute;left:0;top:1081px;width:1188px;height:446px;background:var(--slate)}
.contact .section-title{color:var(--white);top:43px}
.contact-lead{position:absolute;left:262px;top:95px;width:320px;font-size:19px;line-height:23.5px;color:var(--white)}
.contact .field{position:absolute;left:608px;width:287px;height:31px;background:var(--white);border-bottom:3px solid #4f585e;font-size:11px;color:#777;padding:8px 4px}
.send-lg{position:absolute;left:566px;top:354px;width:56px;height:31px;border:1px solid var(--white);color:var(--white);font-size:16px;text-align:center;line-height:29px}

/* news */
.news-card{position:absolute;top:1600px;width:214px}
.news-card .photo{height:121px}
.news-card h4{margin-top:13px;font-size:13.5px;line-height:18px;font-weight:700;color:var(--green-text)}
.news-card p{margin-top:12px;font-size:11px;line-height:14.5px;color:var(--ink-soft)}

/* testimonials */
.testimonials{position:absolute;left:0;top:1927px;width:1188px;height:278px;background:var(--mist)}
.quote{position:absolute;left:312px;top:88px;width:566px;font-size:11px;line-height:17.8px;text-align:center;color:var(--ink-soft)}
.author{position:absolute;left:0;width:1188px;top:189px;text-align:center;font-size:11px;color:var(--green-text)}
.arrow{position:absolute;top:127px;width:18px;height:30px}
.testimonials .btn-outline{left:549px;top:233px;width:91px;height:22px;font-size:12px;line-height:19px;border-width:1px}

/* footer */
.site-footer{position:absolute;left:0;top:2228px;width:1188px;height:261px;background:var(--slate);color:var(--white)}
.footer-head{position:absolute;top:29px;font-size:12px;font-weight:700}
.footer-links{position:absolute;top:54px;list-style:none;font-size:11px;line-height:16.4px}
.newsletter-label{position:absolute;left:726px;top:113px;font-size:12px}
.newsletter-input{position:absolute;left:726px;top:136px;width:200px;height:24px;background:var(--white);color:#777;font-size:12px;padding:4px}
.subscribe{position:absolute;left:726px;top:175px;width:107px;height:30px;border:2px solid var(--white);font-size:16px;text-align:center;line-height:26px}

.chat{position:absolute;left:1139px;top:556px;width:48px;height:48px;border-radius:50%;background:var(--orange);border:2px solid #fff;box-shadow:0 0 3px rgba(0,0,0,.3)}
</style>
</head>
<body>

<header class="site-header">
  <div class="brand"><span class="brand-mark"></span>Harbor Years</div>
  <div class="phone">CALL +555 010 442 310</div>
  <nav class="main-nav"><span>Our services</span><span>Choosing your retirement home</span><span>Our team</span><span>Resources</span></nav>
</header>

<section class="hero">
  <div class="hero-photo" role="img" aria-label="Smiling senior woman with short grey hair in profile against a green chalkboard"></div>
  <h1 class="hero-title serif">Asking the right questions and<br>choosing the right senior housing option</h1>
  <form class="hero-form">
    <div class="field" style="top:81px">Your name</div>
    <div class="field" style="top:109px">Your email</div>
    <div class="field" style="top:137px">Your phone number</div>
    <div class="field" style="top:165px;height:48px">Your message</div>
    <div class="captcha" style="left:625px;top:227px;width:183px;height:46px">
      <span class="box" style="margin-left:8px;width:17px;height:17px"></span>
      <span style="margin-left:8px;font-size:8px">I'm not a robot</span>
      <span class="badge" style="left:150px;top:6px;width:18px;height:18px"></span>
      <small style="left:143px;top:30px">Privacy · Terms</small>
    </div>
    <div class="send-sm">SEND</div>
  </form>
</section>

<section class="services">
  <article class="service" style="left:258px">
    <div class="photo" role="img" aria-label="Counsellor helping an elderly couple at home" style="background:linear-gradient(90deg,#d9d2c8,#b9b0a6 55%,#8f98a6)"><span class="serif">Finding a<br>retirement home</span></div>
    <p>For the last 30 years, our counsellors have helped more than 150,000 families choose their new lifestyle residences, free of charge.</p>
    <div class="btn-outline" style="left:41px">FIND OUT MORE</div>
  </article>
  <article class="service" style="left:489px">
    <div class="photo" role="img" aria-label="Senior woman relaxing in a bright living room" style="background:linear-gradient(90deg,#e8e4dc,#d2c8bb 60%,#ece8e1)"><span class="serif">Additional<br>services</span></div>
    <p>If you need more assistance, we are happy to offer complementary services to help make your transition even smoother.</p>
    <div class="btn-outline" style="left:41px">FIND OUT MORE</div>
  </article>
  <article class="service" style="left:719px">
    <div class="photo" role="img" aria-label="Businesswoman presenting to a group in an office" style="background:linear-gradient(90deg,#c9cfd6,#9ea4ab 50%,#5d5f63)"><span class="serif">Business<br>solutions</span></div>
    <p>Elderway, an efficient partner to help you support your employees in meeting their personal obligations toward an elderly loved one.</p>
    <div class="btn-outline" style="left:41px">FIND OUT MORE</div>
  </article>
</section>

<h2 class="section-title serif" style="top:760px">Why Choose ELDERWAY?</h2>

<div class="feature" style="left:248px;top:812px">
  <svg viewBox="0 0 48 56" style="top:24px"><circle cx="22" cy="18" r="14" fill="none" stroke="#444" stroke-width="3"/><circle cx="22" cy="18" r="8" fill="none" stroke="#444" stroke-width="2"/><path d="M13 29 8 50l7-4 4 7 3-19M31 29l5 21-7-4-4 7-3-19" fill="#444"/></svg>
  <h3 class="serif" style="top:3px">30 years<br>of expertise</h3>
  <p style="top:47px">We are the first and the largest network of Senior Housing Counsellors available everywhere in Quebec and Ontario.</p>
</div>
<div class="feature" style="left:483px;top:812px">
  <svg viewBox="0 0 48 56" style="top:28px"><circle cx="24" cy="24" r="21" fill="none" stroke="#444" stroke-width="3"/><circle cx="24" cy="24" r="16" fill="none" stroke="#444" stroke-width="2"/><text x="24" y="33" text-anchor="middle" font-size="26" font-weight="700" fill="#444" font-family="sans-serif">$</text></svg>
  <h3 class="serif" style="top:15px">Free service</h3>
  <p style="top:38px">Our services are offered free of charge. All costs are covered by the Ontario and Quebec network of private retirement homes.</p>
</div>
<div class="feature" style="left:718px;top:812px">
  <svg viewBox="0 0 56 56" style="top:28px;width:54px"><circle cx="24" cy="24" r="20" fill="none" stroke="#444" stroke-width="3"/><path d="M24 11v13l8 5" fill="none" stroke="#444" stroke-width="3"/><rect x="28" y="34" width="26" height="16" rx="2" fill="#444"/><text x="41" y="47" text-anchor="middle" font-size="12" font-weight="700" fill="#fff" font-family="sans-serif">24h</text></svg>
  <h3 class="serif" style="top:15px">Available 24/7</h3>
  <p style="top:38px">Our counsellors are available 7 days a week. We are on call 24/7 to assist you at every step of your search.</p>
</div>
<div class="feature" style="left:248px;top:948px">
  <svg viewBox="0 0 48 56" style="top:20px"><rect x="6" y="6" width="36" height="46" rx="3" fill="none" stroke="#444" stroke-width="3"/><rect x="16" y="2" width="16" height="8" rx="2" fill="#444"/><path d="M12 20l3 3 5-6M12 32l3 3 5-6M12 44l3 3 5-6" fill="none" stroke="#444" stroke-width="2.5"/><path d="M25 20h11M25 32h11M25 44h11" stroke="#444" stroke-width="2.5"/></svg>
  <h3 class="serif" style="top:5px">Easy process</h3>
  <p style="top:28px">Our 4-step method enables us to understand and analyze your requirements, and propose the best living options.</p>
</div>
<div class="feature" style="left:483px;top:948px">
  <svg viewBox="0 0 48 56" style="top:18px"><path d="M24 30C10 20 4 14 6 8c2-6 11-7 18 2 7-9 16-8 18-2 2 6-4 12-18 22z" fill="#444"/><path d="M3 22c1 10 8 18 18 26l-3 6C8 46 2 36 3 22zM45 22c-1 10-8 18-18 26l3 6c10-8 16-18 15-32z" fill="#444"/></svg>
  <h3 class="serif" style="top:5px">Respectful</h3>
  <p style="top:28px">A process based on respect. We share your concerns, and our goal is to respond by helping you find the ideal living situation.</p>
</div>
<div class="feature" style="left:718px;top:948px">
  <svg viewBox="0 0 48 56" style="top:22px"><circle cx="13" cy="8" r="6" fill="#444"/><circle cx="35" cy="8" r="6" fill="#444"/><path d="M4 18h18v16h-4v16h-10V34H4zM26 18h18v16h-4v16H30V34h-4z" fill="#444"/><path d="M20 26h8" stroke="#444" stroke-width="3"/></svg>
  <h3 class="serif" style="top:-7px">Reliable<br>partners</h3>
  <p style="top:36px">A network of reliable and complementary partners to accompany you and facilitate your transition to a residence.</p>
</div>

<section class="contact">
  <h2 class="section-title serif">Contact-us, the service is free</h2>
  <p class="contact-lead">Our counsellors are available and happy to meet you to discuss the options and help you select the ideal assisted living residence for you or your loved one.</p>
  <form>
    <div class="field" style="top:99px">Your name</div>
    <div class="field" style="top:134px">Your email</div>
    <div class="field" style="top:169px">Phone number</div>
    <div class="field" style="top:204px;height:64px;border-bottom:0">Your message</div>
    <div class="captcha" style="left:505px;top:294px;width:183px;height:46px">
      <span class="box" style="margin-left:8px;width:17px;height:17px"></span>
      <span style="margin-left:8px;font-size:8px">I'm not a robot</span>
      <span class="badge" style="left:150px;top:6px;width:18px;height:18px"></span>
      <small style="left:143px;top:30px">Privacy · Terms</small>
    </div>
    <div class="send-lg">SEND</div>
  </form>
</section>

<h2 class="section-title serif" style="top:1553px;left:6px">Latest News</h2>
<article class="news-card" style="left:262px">
  <div class="photo" role="img" aria-label="Elderly couple embracing and laughing" style="background:linear-gradient(90deg,#bdb7ae,#d8d2c9 55%,#eceae6)"></div>
  <h4>Some tips that will make the life of the elderly much easier and more enjoyable</h4>
  <p>Making the lives of older people much easier and more enjoyable is probably easier than you think. There are strategies that are often both simple and quick to put in place.</p>
</article>
<article class="news-card" style="left:491px">
  <div class="photo" role="img" aria-label="Grandparents and grandchildren posing for a family photo on a sofa" style="background:linear-gradient(90deg,#5a4630,#b08a5c 45%,#d9c4a4 70%,#7a5a3a)"></div>
  <h4>Residence for the elderly: 3 important steps before making your choice</h4>
  <p>Finding and choosing the right home for the elderly is a decision that can be difficult. Being accompanied by a qualified, specialized person who is attentive to the needs of his/her clientele will help you make the right decision.</p>
</article>
<article class="news-card" style="left:719px">
  <div class="photo" role="img" aria-label="Advisor meeting an elderly couple at a table" style="background:linear-gradient(90deg,#c9b99f,#e6dccb 40%,#a84a3a 60%,#d8cbb5)"></div>
  <h4>How to choose the right Senior Housing Facility or Retirement Home</h4>
  <p>Searching for a retirement home or a senior housing facility is quite an important step in life because not all retirement residence offer the same quality of senior care and services for seniors. There is a wide range of retirement homes to choose from.</p>
</article>

<section class="testimonials">
  <h2 class="section-title serif" style="top:27px">Testimonials</h2>
  <svg class="arrow" viewBox="0 0 18 30" style="left:262px"><path d="M16 0v30L0 15z" fill="var(--orange)"/></svg>
  <p class="quote">Dana clearly went above and beyond her job description throughout this process. This included after hours telephone and text messages from me, transportation of my Mom and her walker, lengthy telephone calls with my Mom, touring retirement home facilities...and solving a crisis ( or two) along the way. Dana was excellent with my Mom throughout this time. Patient, understanding, caring and exemplifying tremendous empathy are words that come to mind for me describing Dana helping both my Mom and I.</p>
  <svg class="arrow" viewBox="0 0 18 30" style="left:909px"><path d="M2 0v30l16-15z" fill="var(--orange)"/></svg>
  <p class="author">- Gordon, Kingston</p>
  <div class="btn-outline">READ MORE</div>
</section>

<footer class="site-footer">
  <div class="footer-head" style="left:262px">CONTACT US</div>
  <div class="footer-head" style="left:407px">SITE MAP</div>
  <ul class="footer-links" style="left:407px">
    <li>Home</li><li>Our Services</li><li>Our Team</li><li>Finding a retirement home</li><li>Business solutions</li><li>Choosing your retirement</li><li>home</li><li>Why choose Elderway?</li><li>Your needs</li><li>Type of residence</li>
  </ul>
  <ul class="footer-links" style="left:567px">
    <li>Elderway in your region</li><li>Our senior living advisors</li><li>Additionnal services</li><li>FAQ</li><li>Testimonials</li><li>News</li><li>Useful Links</li><li>Careers</li><li>Contact</li>
  </ul>
  <div class="footer-head" style="left:726px">FOLLOW US</div>
  <div class="newsletter-label">NEWSLETTER</div>
  <div class="newsletter-input">Your Email</div>
  <div class="subscribe">SUBSCRIBE</div>
</footer>

<div class="chat"><svg viewBox="0 0 44 44" width="44" height="44"><ellipse cx="22" cy="21" rx="10" ry="8" fill="#fff"/><path d="M15 26l-2 6 7-4z" fill="#fff"/><circle cx="18" cy="21" r="1.3" fill="var(--orange)"/><circle cx="22" cy="21" r="1.3" fill="var(--orange)"/><circle cx="26" cy="21" r="1.3" fill="var(--orange)"/></svg></div>

</body>
</html>
```